Up and coming mattress store needs a better website design

We are a family owned mattress store called QR Bedding and we are in need of a better looking website. We have started advertising online and our current website qrbeddingshop.com is really bad. We are looking for at lest 4 pages including: welcome page, about us page, our mattresses page, and contact us page. Here is a wire frame of something I was thinking of https://mockboard.example/7kq2ZP it doesn't have to be like this it is just an idea. Some must haves are: Name, Logo, at lest 3 spots for links for financing, a bigger spot for special offers, maybe the number and address for the store at the very bottom. You can submit a one page welcome design to start with and if I like it we can move on from there. Thank you for your time!

Target Market(s)

20 to 40 year olds who want to buy mattresses

Industry/Entity Type

Store

Coding

Coded - Design and coding required

Number of Pages Required

4 page

Requirements
Must have
• name, logo, 3 spots for links for our no credit check financing companies
Nice to have
• All stores addresses and numbers at the bottom: Main Store 2418 Tolliver Hwy South Houston 77590 (346)-555-0182 Smaller Store 2207 Hwy 9 Alvin Tx 77514 (281)-555-0139

```html
<!DOCTYPE html>
<html lang="en">
<head>
<meta charset="utf-8">
<title>QR Bedding – Welcome</title>
<link href="https://fonts.googleapis.com/css2?family=Open+Sans:wght@400;600;700&family=Raleway:wght@400;500;600&display=swap" rel="stylesheet">
<style>
  :root {
    --red: #e3262b;
    --ink: #333333;
    --muted: #777777;
    --band: #f4f4f4;
    --line: #e6e6e6;
    --footer: #2b2b30;
    --footer-deep: #222226;
    --footer-line: #3c3c42;
    --footer-text: #8a8a90;
    --white: #ffffff;
  }
  * { margin: 0; padding: 0; box-sizing: border-box; }
  html, body { width: 678px; height: 1200px; overflow: hidden; background: var(--white); }
  body { font-family: "Open Sans", Arial, sans-serif; color: var(--ink); position: relative; }
  .abs { position: absolute; }

  /* Hero */
  .hero { left: 0; top: 0; width: 678px; height: 370px;
    background: linear-gradient(180deg, #8d7c66 0%, #a8957c 35%, #7b6a57 70%, #5a4a3b 100%); }
  .brand { left: 56px; top: 38px; display: flex; align-items: center; gap: 5px; }
  .brand-mark { width: 14px; height: 14px; border-radius: 50%; background: var(--red); }
  .brand-name { font-family: "Raleway", sans-serif; font-weight: 600; font-size: 16px; color: var(--red); }
  .nav { top: 27px; font-size: 8px; color: var(--white); font-weight: 600; }
  .nav.active { color: var(--red); }
  .offer-panel { left: 57px; top: 122px; width: 565px; height: 156px; background: rgba(60,58,56,0.72);
    display: flex; align-items: center; justify-content: center; text-align: center; }
  .offer-panel p { font-family: "Raleway", sans-serif; font-size: 19px; line-height: 29.5px; color: var(--white); width: 530px; }
  .dot { top: 345px; width: 6px; height: 6px; border-radius: 50%; background: rgba(255,255,255,0.6); }
  .dot.on { background: var(--red); }

  /* Welcome */
  .welcome-title { left: 0; width: 678px; top: 393px; text-align: center; font-family: "Raleway", sans-serif; font-size: 15px; }
  .accent { color: var(--red); }
  .welcome-text { left: 80px; width: 518px; top: 422px; text-align: center; font-size: 7.5px; line-height: 12px; color: var(--muted); }
  .divider { left: 70px; width: 540px; top: 464px; height: 1px; background: var(--line); }
  .feature { width: 140px; top: 482px; text-align: center; }
  .feature svg { display: block; margin: 0 auto; }
  .feature h3 { font-size: 9.5px; font-weight: 600; margin-top: 12px; color: var(--ink); }
  .feature h3.accent { color: #b8161b; }
  .feature p { font-size: 6.5px; line-height: 11.5px; color: var(--muted); margin-top: 5px; }

  /* Info band */
  .info-band { left: 0; top: 633px; width: 678px; height: 136px; background: var(--band); }
  .info-col { top: 662px; width: 172px; }
  .info-head { display: flex; align-items: center; gap: 7px; font-family: "Raleway", sans-serif; font-size: 14px; }
  .initial { width: 26px; height: 22px; border: 1px solid var(--red); color: var(--red); display: flex; align-items: center; justify-content: center; font-size: 13px; }
  .info-col p { font-size: 6.5px; line-height: 11.5px; color: var(--muted); margin-top: 9px; text-align: justify; }
  .contact-lines { margin-top: 9px; font-size: 6.5px; line-height: 15px; color: var(--muted); }
  .contact-lines b { font-weight: 400; color: var(--ink); }

  /* Financing */
  .finance-title { left: 0; width: 678px; top: 795px; text-align: center; font-family: "Raleway", sans-serif; font-size: 15px; }
  .finance-card { top: 834px; width: 185px; text-align: center; }
  .finance-photo { width: 185px; height: 108px; }
  .finance-card h3 { font-size: 9.5px; font-weight: 600; margin-top: 18px; }
  .finance-card p { font-size: 6.5px; line-height: 11.5px; color: var(--muted); margin-top: 8px; padding: 0 8px; }

  /* Footer */
  .footer { left: 0; top: 1043px; width: 678px; height: 112px; background: var(--footer); }
  .footer-box { top: 1074px; width: 176px; height: 52px; border: 1px solid var(--footer-line); }
  .footer-icon { position: absolute; left: 9px; top: 10px; width: 26px; height: 26px; border-radius: 50%; background: var(--red);
    display: flex; align-items: center; justify-content: center; }
  .footer-box h4 { position: absolute; left: 49px; top: 8px; font-family: "Raleway", sans-serif; font-weight: 500; font-size: 10px; color: var(--white); }
  .footer-box p { position: absolute; left: 49px; top: 25px; width: 120px; font-size: 6.3px; line-height: 11px; color: var(--footer-text); }
  .bottom-bar { left: 0; top: 1155px; width: 678px; height: 45px; background: var(--footer-deep); }
  .copyright { left: 56px; top: 1173px; font-size: 7px; color: #55555b; }
  .social { top: 1169px; width: 17px; height: 17px; border-radius: 2px; }
</style>
</head>
<body>

<div class="abs hero" role="img" aria-label="Bedroom with a made mattress on a low upholstered bed, warm wall lamps and curtains"></div>
<div class="abs brand"><span class="brand-mark"></span><span class="brand-name">QR Bedding</span></div>
<span class="abs nav active" style="left:226px">Home</span>
<span class="abs nav" style="left:280px">About Us</span>
<span class="abs nav" style="left:346px">Service</span>
<span class="abs nav" style="left:406px">Financing</span>
<span class="abs nav" style="left:473px">Special Offers</span>
<span class="abs nav" style="left:553px">Conatct Us</span>
<svg class="abs" style="left:621px;top:28px" width="9" height="9" viewBox="0 0 10 10" aria-label="Search"><circle cx="4" cy="4" r="3" fill="none" stroke="#fff" stroke-width="1.6"/><line x1="6.3" y1="6.3" x2="9" y2="9" stroke="#fff" stroke-width="1.8"/></svg>

<div class="abs offer-panel"><p>Special Offers like about us having name brand mattresses at %80 retail, #1 rated mattresses, gel foam mattress sales, maybe some multiple ads sideways scrolling</p></div>
<span class="abs dot" style="left:312px"></span>
<span class="abs dot on" style="left:335px"></span>
<span class="abs dot" style="left:356px"></span>

<h2 class="abs welcome-title">Welcome To <span class="accent">QR Bedding</span></h2>
<p class="abs welcome-text">There are many variations of passages of Lorem Ipsum available, but the majority have suffered alteration in some form, by injected humour, or randomised words which don't look even slightly believable. If you are going to use a passage of Lorem Ipsum, you need</p>
<div class="abs divider"></div>

<div class="abs feature" style="left:50px">
  <svg width="58" height="58" viewBox="0 0 58 58"><circle cx="29" cy="29" r="26" fill="none" stroke="#e3262b" stroke-width="5"/><line x1="3" y1="29" x2="55" y2="29" stroke="#fff" stroke-width="3"/><rect x="19" y="20" width="20" height="14" rx="3" fill="#e3262b"/><rect x="21" y="34" width="3" height="4" fill="#e3262b"/><rect x="34" y="34" width="3" height="4" fill="#e3262b"/><circle cx="29" cy="25" r="3" fill="#fff"/></svg>
  <h3 class="accent">Finibus Bonorum</h3>
  <p>There are many variations of passages of Lorem Ipsum available, but the majority have suffered alteration in some ...</p>
</div>
<div class="abs feature" style="left:196px">
  <svg width="58" height="58" viewBox="0 0 58 58"><circle cx="29" cy="29" r="27" fill="none" stroke="#e3262b" stroke-width="1.3"/><path d="M17 24 L29 16 L41 24" fill="none" stroke="#e3262b" stroke-width="2"/><rect x="20" y="30" width="18" height="5" fill="none" stroke="#e3262b" stroke-width="1.6"/><line x1="20" y1="27" x2="20" y2="39" stroke="#e3262b" stroke-width="1.6"/><line x1="38" y1="32" x2="38" y2="39" stroke="#e3262b" stroke-width="1.6"/></svg>
  <h3>Facere possimus</h3>
  <p>There are many variations of passages of Lorem Ipsum available, but the majority have suffered alteration in some ...</p>
</div>
<div class="abs feature" style="left:341px">
  <svg width="58" height="58" viewBox="0 0 58 58"><circle cx="29" cy="29" r="27" fill="none" stroke="#e3262b" stroke-width="1.3"/><rect x="16" y="29" width="26" height="6" fill="#e3262b"/><rect x="16" y="24" width="3" height="14" fill="#e3262b"/><rect x="39" y="27" width="3" height="11" fill="#e3262b"/><rect x="21" y="25" width="6" height="4" rx="1" fill="#e3262b"/></svg>
  <h3>Nam libero tempore</h3>
  <p>There are many variations of passages of Lorem Ipsum available, but the majority have suffered alteration in some ...</p>
</div>
<div class="abs feature" style="left:487px">
  <svg width="58" height="58" viewBox="0 0 58 58"><circle cx="29" cy="29" r="27" fill="none" stroke="#e3262b" stroke-width="1.3"/><rect x="18" y="25" width="22" height="10" rx="2" fill="#e3262b"/><line x1="18" y1="30" x2="40" y2="30" stroke="#fff" stroke-width="1"/><path d="M16 38 q3 -2 6 0 t6 0 t6 0 t6 0" fill="none" stroke="#e3262b" stroke-width="1.4"/></svg>
  <h3>Praesentium voluptatum</h3>
  <p>There are many variations of passages of Lorem Ipsum available, but the majority have suffered alteration in some ...</p>
</div>

<div class="abs info-band"></div>
<div class="abs info-col" style="left:56px">
  <div class="info-head"><span class="initial">A</span>BOUT US</div>
  <p>Nemo enim ipsam voluptatem quia voluptas sit aspernatur aut odit aut fugit, sed quia consequuntur magni dolores eos qui ratione voluptatem sequi nesciunt. Neque porro quisquam est, qui dolorem...</p>
</div>
<div class="abs info-col" style="left:256px">
  <div class="info-head"><span class="initial">M</span>ATTRESS</div>
  <p>Nemo enim ipsam voluptatem quia voluptas sit aspernatur aut odit aut fugit, sed quia consequuntur magni dolores eos qui ratione voluptatem sequi nesciunt. Neque porro quisquam est, qui dolorem...</p>
</div>
<div class="abs info-col" style="left:449px;width:190px">
  <div class="info-head"><span class="initial">C</span>ONTACT US</div>
  <div class="contact-lines">
    <div><b>ADDRESS</b> : Main Store 2418 Tolliver Hwy South Houston</div>
    <div><b>PHONE NUMBER</b> : 77590 (346)-555-0182</div>
    <div><b>FAX</b> : 77514 (281)-555-0139</div>
  </div>
</div>

<h2 class="abs finance-title"><span class="accent">Mattress</span> Financing</h2>
<div class="abs finance-card" style="left:56px">
  <div class="finance-photo" role="img" aria-label="Person resting on a soft white pillow" style="background:linear-gradient(135deg,#d9cdb8,#f3efe8 55%,#e8e4de)"></div>
  <h3>Excepteur sint occaecat</h3>
  <p>Sed ut perspiciatis unde omnis is natus voluptatem accusantium doloremque laudantium, totam aperiam, eaque ipsa quae ab illo inventore veritatis quasi</p>
</div>
<div class="abs finance-card" style="left:246px">
  <div class="finance-photo" role="img" aria-label="Warm wood-panelled bedroom with a made bed and pendant lamp" style="background:linear-gradient(160deg,#6b4a2c,#b0804f 50%,#4a3222)"></div>
  <h3>Accusamus et iusto</h3>
  <p>Sed ut perspiciatis unde omnis is natus voluptatem accusantium doloremque laudantium, totam aperiam, eaque ipsa quae ab illo inventore veritatis quasi</p>
</div>
<div class="abs finance-card" style="left:437px">
  <div class="finance-photo" role="img" aria-label="White pillows on a bed beside a bedside lamp" style="background:linear-gradient(200deg,#e2b77a,#efe6da 45%,#dcdde3)"></div>
  <h3>Et harum quidem</h3>
  <p>Sed ut perspiciatis unde omnis is natus voluptatem accusantium doloremque laudantium, totam aperiam, eaque ipsa quae ab illo inventore veritatis quasi</p>
</div>

<div class="abs footer"></div>
<div class="abs footer-box" style="left:56px">
  <span class="footer-icon"><svg width="12" height="11" viewBox="0 0 12 11"><path d="M6 0 L12 5 H10 V11 H7 V7 H5 V11 H2 V5 H0 Z" fill="#fff"/></svg></span>
  <h4>Contact Us</h4>
  <p>Main Store 2418 Tolliver Hwy South Houston</p>
</div>
<div class="abs footer-box" style="left:251px">
  <span class="footer-icon"><svg width="12" height="11" viewBox="0 0 12 11"><path d="M6 0 L12 5 H10 V11 H7 V7 H5 V11 H2 V5 H0 Z" fill="#fff"/></svg></span>
  <h4>Quick Contact</h4>
  <p>PH : 77590 (346)-555-0182<br>FAX : 77514 (281)-555-0139</p>
</div>
<div class="abs footer-box" style="left:446px">
  <span class="footer-icon"><svg width="12" height="11" viewBox="0 0 12 11"><path d="M6 0 L12 5 H10 V11 H7 V7 H5 V11 H2 V5 H0 Z" fill="#fff"/></svg></span>
  <h4>Mail Us On</h4>
  <p>info@qrbeddingshop.com / www.qrbeddingshop.com</p>
</div>

<div class="abs bottom-bar"></div>
<p class="abs copyright">Copyrights@2016 QR Bedding . All Rights Reserved</p>
<span class="abs social" style="left:540px;background:#3b5b9a"></span>
<span class="abs social" style="left:562px;background:#4aa3d8"></span>
<span class="abs social" style="left:584px;background:#2a79b0"></span>
<span class="abs social" style="left:606px;background:#e8892b"></span>

</body>
</html>
```